Hollowmere Farm Promotional Leaflet

The team at Hollowmere Farm can help with every aspect of managing and enhancing your home from housekeeping and professional cleaning, laundry and ironing to providing chic and contemporary flower arrangements and even food for your pets!We take pride in providing high-end, consistent and reliable professional services bespoke to you. Whether you are a busy professional working long hours, a stay-at home parent or retired; having professional help in the home gives you time to spend on the things you enjoy.We are providing a very upmarket, highly professional service and need an A5 promotional leaflet to be designed. Please refer to www.hollowmerefarm.example.co.uk and see the section on 'Home Management'The leaflet should incorporate the Hollowmere Farm logo without the 'tipi', and any suitable photography images used on the home page of the website or the 'home management' section.

Target Market(s)

high-end, affluent owners of luxury homes

Industry/Entity Type

Farm

Contact Information for Business Card

The business card design needs to be suitable for use across all of Hollowmere Farm businesses, specifically:
Hollowmere Farm Home Management - otherwise known as Hollowmere Farm @ Home (this uses the typographical logo
Hollowmere Farm Weddings & Events - this uses the 'tipi' logo

Requirements
Must have
• Design in keeping with the look and feel of the logo and website design
• www.hollowmerefarm.example.co.uk

```html
<!DOCTYPE html>
<html lang="en">
<head>
<meta charset="utf-8">
<title>Hollowmere Farm Home Management – A5 Leaflet</title>
<link rel="stylesheet" href="https://fonts.googleapis.com/css2?family=Libre+Bodoni:ital,wght@0,400;1,400&display=swap">
<style>
  :root {
    --backdrop: #dcdcdc;
    --paper: #ffffff;
    --magenta: #d82262;
    --brand-pink: #e0679a;
    --ink: #555555;
    --rule: #a9a9a9;
    --on-magenta: #ffffff;
    --frame: #ffffff;
  }
  * { box-sizing: border-box; margin: 0; padding: 0; }
  html, body { width: 1200px; height: 900px; overflow: hidden; }
  body {
    background: var(--backdrop);
    font-family: "Libre Bodoni", "Bodoni Moda", Georgia, serif;
    font-style: italic;
    color: var(--ink);
    position: relative;
  }
  .page {
    position: absolute;
    top: 56px;
    width: 509px;
    height: 722px;
    background: var(--paper);
    overflow: hidden;
  }
  .page--front { left: 81px; }
  .page--back { left: 611px; }

  .band { position: absolute; left: 0; width: 100%; background: var(--magenta); }

  .photo {
    position: absolute;
    border: 6px solid var(--frame);
    box-shadow: 2px 3px 6px rgba(0,0,0,.25);
  }

  .titled-rule {
    position: absolute; left: 0; width: 100%;
    display: flex; align-items: center; gap: 14px;
    font-size: 21px; color: var(--ink); white-space: nowrap;
  }
  .titled-rule::before, .titled-rule::after {
    content: ""; flex: 1; height: 1px; background: var(--rule);
  }

  /* Front */
  .front__tagline {
    position: absolute; top: 62px; left: 0; width: 100%;
    text-align: center; color: var(--on-magenta);
    font-size: 20px; line-height: 27px;
  }
  .front__photo {
    left: 102px; top: 188px; width: 310px; height: 222px;
    background: linear-gradient(160deg, #8a7d72 0%, #cfc4b8 45%, #b7aa9c 70%, #6e6259 100%);
  }
  .front__wordmark {
    position: absolute; top: 552px; left: 0; width: 100%;
    text-align: center; font-style: normal;
    font-size: 40px; color: var(--brand-pink);
  }
  .front__url {
    position: absolute; top: 652px; left: 0; width: 100%;
    text-align: center; font-size: 18px; color: var(--magenta);
  }

  /* Back */
  .back__intro {
    position: absolute; left: 35px; top: 92px; width: 450px;
    color: var(--on-magenta); font-size: 14px; line-height: 18px;
  }
  .bullets { position: absolute; list-style: none; font-size: 14px; line-height: 17.5px; }
  .bullets li { position: relative; padding-left: 20px; }
  .bullets li::before { content: "•"; position: absolute; left: 0; font-style: normal; }
  .bullets--light { color: var(--on-magenta); }
  .bullets--dark { color: var(--ink); }

  .back__wardrobe {
    left: 374px; top: 117px; width: 135px; height: 108px;
    background: linear-gradient(135deg, #6b5446, #b9a89b 55%, #8d7a6c);
  }
  .back__lounge {
    left: 18px; top: 268px; width: 165px; height: 175px;
    transform: rotate(-17deg);
    background: linear-gradient(160deg, #e3e0dc 0%, #bdb8b2 50%, #2e3550 100%);
  }
  .back__kitchen {
    left: 352px; top: 460px; width: 144px; height: 94px;
    background: linear-gradient(180deg, #e9e4dc 0%, #d6cfc4 45%, #2d3636 100%);
  }
  .back__copy { position: absolute; font-size: 14px; line-height: 17.5px; color: var(--ink); }
  .back__footer {
    position: absolute; left: 0; top: 623px; width: 100%;
    text-align: center; font-size: 11px; line-height: 15px; color: var(--magenta);
  }
  .back__footer .lead { font-size: 14px; line-height: 18px; color: var(--ink); }
</style>
</head>
<body>

<section class="page page--front" aria-label="Leaflet front">
  <div class="band" style="top:0;height:322px;"></div>
  <p class="front__tagline">Taking pride in providing high-end, consistent<br>and reliable professional services<br>bespoke to you</p>
  <div class="photo front__photo" role="img" aria-label="Photo of an elegant living room with cream sofas, fireplace and chandelier"></div>
  <h2 class="titled-rule" style="top:458px;font-weight:400;">Hollowmere Farm Home Management</h2>
  <p class="front__wordmark">Hollowmere Farm</p>
  <p class="front__url">www.hollowmerefarm.example.co.uk</p>
</section>

<section class="page page--back" aria-label="Leaflet back">
  <h2 class="titled-rule" style="top:30px;font-size:20px;font-weight:400;">Hollowmere Farm Home Management</h2>
  <div class="band" style="top:74px;height:265px;"></div>

  <p class="back__intro">The team @ Hollowmere Farm can help with every aspect of managing and enhancing your home including:</p>
  <ul class="bullets bullets--light" style="left:48px;top:139px;">
    <li>Regular housekeeping and professional cleaning</li>
    <li>Exit cleans</li>
    <li>One-off seasonal /party / building work cleans</li>
    <li>Laundry and ironing</li>
  </ul>
  <div class="photo back__wardrobe" role="img" aria-label="Photo of a woman seated in a walk-in wardrobe with a dog"></div>
  <ul class="bullets bullets--light" style="left:184px;top:235px;">
    <li>Chic and contemporary flower arrangements</li>
    <li>Car valeting</li>
    <li>Pet food delivery</li>
    <li>Dry cleaning</li>
  </ul>
  <div class="photo back__lounge" role="img" aria-label="Photo of a woman relaxing on a navy sofa with a small dog"></div>

  <p class="back__copy" style="left:248px;top:350px;width:240px;">We take pride in providing high-end, consistent and reliable professional services bespoke to you.</p>
  <p class="back__copy" style="left:164px;top:416px;width:320px;">Coming home to a beautiful environment and being able to relax and enjoy your time is something we all deserve.</p>

  <ul class="bullets bullets--dark" style="left:48px;top:479px;">
    <li>Satisfaction guaranteed</li>
    <li>Professional staff you can trust and rely on</li>
    <li>Competitive rates</li>
  </ul>
  <div class="photo back__kitchen" role="img" aria-label="Photo of a country kitchen with dark cabinetry and range hood"></div>
  <ul class="bullets bullets--dark" style="left:106px;top:544px;">
    <li>CRB checked and referenced</li>
    <li>Member of the Household Staffing Guild</li>
    <li>Fully Insured</li>
  </ul>

  <div class="back__footer">
    <p class="lead">We look after our clients’ homes and holiday lets across South Somerset.</p>
    <p>Contact us to arrange a home visit and quotation:</p>
    <p>E: info@hollowmerefarm.example.co.uk</p>
    <p>T: 07700 900416</p>
    <p>www.hollowmerefarm.example.co.uk</p>
  </div>
</section>

</body>
</html>
```